Personal training and nutrition business needs business card design

We need a business card that outlays our services and invites potential customers to join our team and take the first step to a healthier and more enjoyable life. We cater for any level of fitness and specialize in weight loss and conditioning, strength training, muscle gain and strength endurance. Whether you are just starting off or need some help getting to the next level of your journey we are here to get the job done.
We specialize in one on one or one on two personal training sessions and each program will be custom made to suit individual fitness goals of our clients

```html
<!DOCTYPE html>
<html lang="en">
<head>
<meta charset="utf-8">
<title>Stride &amp; Steady – Business Card</title>
<link href="https://fonts.googleapis.com/css2?family=Arimo:wght@400;700&family=Oswald:wght@400&display=swap" rel="stylesheet">
<style>
  :root {
    --bg: #e4e4e2;
    --card: #2f2f31;
    --purple: #a055c4;
    --purple-light: #c06cc8;
    --purple-deep: #7a45b8;
    --white: #f4f4f4;
    --muted: #d8d8d8;
  }
  * { box-sizing: border-box; margin: 0; padding: 0; }
  html, body { width: 1200px; height: 801px; overflow: hidden; }
  body {
    background: var(--bg);
    font-family: "Arimo", Arial, sans-serif;
    position: relative;
  }
  .card {
    position: absolute;
    top: 252px;
    width: 520px;
    height: 297px;
    background: var(--card);
    border-bottom: 5px solid var(--purple);
    border-image: linear-gradient(90deg, var(--purple-deep), var(--purple-light)) 1;
    box-shadow: 0 6px 18px rgba(0,0,0,.18);
    overflow: hidden;
  }
  .card--front { left: 53px; }
  .card--back { left: 627px; }

  /* front */
  .person {
    position: absolute;
    top: 28px;
    right: 30px;
    text-align: right;
  }
  .person__name {
    color: var(--purple);
    font-size: 19px;
    font-weight: 700;
    letter-spacing: .5px;
  }
  .person__role {
    color: var(--white);
    font-size: 14px;
    margin-top: 3px;
  }
  .person__address {
    color: var(--white);
    font-size: 13px;
    line-height: 1.45;
    margin-top: 14px;
  }
  .brand {
    position: absolute;
    left: 30px;
    top: 92px;
  }
  .brand__row { display: flex; align-items: center; gap: 10px; }
  .brand__mark {
    width: 16px; height: 16px;
    background: var(--purple);
    border-radius: 3px;
  }
  .brand__name {
    color: var(--white);
    font-weight: 700;
    font-size: 28px;
    letter-spacing: 1px;
    text-transform: uppercase;
  }
  .brand__tagline {
    font-family: "Oswald", "Arial Narrow", sans-serif;
    color: var(--purple-light);
    font-size: 10px;
    letter-spacing: 1.3px;
    margin-top: 6px;
    text-transform: uppercase;
  }
  .contacts {
    position: absolute;
    left: 30px;
    bottom: 28px;
    list-style: none;
  }
  .contacts li {
    display: flex;
    align-items: center;
    gap: 10px;
    color: var(--white);
    font-size: 14px;
    line-height: 1.65;
  }
  .contacts svg { width: 13px; height: 13px; flex: none; }

  /* back */
  .card--back .brand {
    left: auto;
    right: 34px;
    top: auto;
    bottom: 56px;
    text-align: left;
  }
  .card--back .brand__name { font-size: 34px; }
</style>
</head>
<body>
  <section class="card card--front">
    <div class="person">
      <div class="person__name">DANIEL REYES</div>
      <div class="person__role">Manager</div>
      <div class="person__address">Your address<br>city, state, ZIP 0000</div>
    </div>

    <div class="brand">
      <div class="brand__row">
        <span class="brand__mark"></span>
        <span class="brand__name">Stride &amp; Steady</span>
      </div>
      <div class="brand__tagline">Personal training. Nutrition. Motivation</div>
    </div>

    <ul class="contacts">
      <li>
        <svg viewBox="0 0 24 24" fill="var(--purple)"><path d="M6.6 10.8a15 15 0 0 0 6.6 6.6l2.2-2.2a1 1 0 0 1 1-.25 11.4 11.4 0 0 0 3.6.57 1 1 0 0 1 1 1V20a1 1 0 0 1-1 1A17 17 0 0 1 3 4a1 1 0 0 1 1-1h3.5a1 1 0 0 1 1 1c0 1.25.2 2.45.57 3.57a1 1 0 0 1-.25 1z"/></svg>
        555-014-2100
      </li>
      <li>
        <svg viewBox="0 0 24 24" fill="none" stroke="var(--purple)" stroke-width="2"><rect x="3" y="5" width="18" height="14"/><path d="M3 6l9 7 9-7"/></svg>
        hello@stridesteady.com
      </li>
      <li>
        <svg viewBox="0 0 24 24" fill="none" stroke="var(--purple)" stroke-width="2"><circle cx="12" cy="12" r="9"/><path d="M3 12h18M12 3c3 3 3 15 0 18M12 3c-3 3-3 15 0 18"/></svg>
        www.stridesteady.com
      </li>
    </ul>
  </section>

  <section class="card card--back">
    <div class="brand">
      <div class="brand__row">
        <span class="brand__name">Stride &amp; Steady</span>
      </div>
      <div class="brand__tagline">Personal training. Nutrition. Motivation</div>
    </div>
  </section>
</body>
</html>
```